Bramwell Resources Ltd. - Refreshed business card challenge

A revised, refreshed business card design for my oil and gas company using my existing logo. Feel free to be as creative as you like!

Target Market(s)

bankers, lawyers

Industry/Entity Type

Oil And Gas Exploration

Contact Information for Business Card

See the "Must Haves" section

Font styles to use
Serif
Sans Serif

Colors

Designer to choose colors to be used in the design.

Requirements
Must have
• Existing business logo, name, title, email, phone number, business address
• Neil Hadley, CA, CPA
• Vice President Finance & Chief Financial Officer
• nhadley@bramwellresources-mail.com
• office: (587)555-0142
• cell: (403)555-0187
• 1400, 815 4 Street S.W.
• Calgary, AB
• T2P 4K8
Should not have
• Should not be plain and boring.

```html
<!DOCTYPE html>
<html lang="en">
<head>
<meta charset="utf-8">
<title>Bramwell Resources Ltd. — Business Card</title>
<link rel="stylesheet" href="https://fonts.googleapis.com/css2?family=Roboto:wght@300;400;700&display=swap">
<style>
  :root {
    --backdrop: #e6e6e6;
    --card-white: #ffffff;
    --card-grey: #acacac;
    --card-grey-light: #b8b8b8;
    --brand-green: #1f5a2c;
    --ink: #6f6f6f;
    --ink-soft: #9a9a9a;
    --watermark: #ececec;
  }
  * { box-sizing: border-box; margin: 0; padding: 0; }
  html, body {
    width: 1200px;
    height: 1048px;
    overflow: hidden;
    background: var(--backdrop);
    font-family: "Roboto", sans-serif;
  }
  .stage {
    position: relative;
    width: 1200px;
    height: 1048px;
    display: flex;
    align-items: center;
    justify-content: center;
    gap: 40px;
  }
  .card {
    position: relative;
    width: 540px;
    height: 309px;
    overflow: hidden;
    box-shadow: 0 2px 6px rgba(0,0,0,0.12);
  }

  /* Front */
  .card-front {
    background: var(--card-white);
    clip-path: polygon(0 0, 100% 0, 100% 82%, 94% 100%, 0 100%);
  }
  .contact-name {
    position: absolute;
    left: 44px;
    top: 44px;
    font-size: 17px;
    font-weight: 700;
    color: var(--brand-green);
    letter-spacing: 0.02em;
  }
  .contact-name .credentials {
    font-weight: 300;
    color: var(--ink-soft);
    font-size: 13px;
    margin-left: 4px;
  }
  .contact-title {
    position: absolute;
    left: 44px;
    top: 72px;
    font-size: 10px;
    line-height: 1.45;
    color: var(--ink);
    text-transform: uppercase;
    letter-spacing: 0.06em;
  }
  .contact-address {
    position: absolute;
    left: 44px;
    top: 176px;
    font-size: 10px;
    line-height: 1.5;
    color: var(--ink);
    text-transform: uppercase;
    letter-spacing: 0.05em;
  }
  .contact-lines {
    position: absolute;
    left: 44px;
    top: 226px;
    font-size: 10px;
    line-height: 1.6;
    color: var(--ink);
    letter-spacing: 0.04em;
  }
  .contact-lines .label { font-weight: 700; margin-right: 3px; }
  .contact-lines .sep { margin: 0 6px; color: var(--ink-soft); }
  .website {
    position: absolute;
    right: 82px;
    top: 246px;
    font-size: 10px;
    color: var(--ink);
    text-transform: uppercase;
    letter-spacing: 0.06em;
  }
  .name-watermark {
    position: absolute;
    right: 12px;
    top: 18px;
    writing-mode: vertical-rl;
    font-size: 46px;
    font-weight: 700;
    color: var(--watermark);
    letter-spacing: 0.01em;
  }

  /* Back */
  .card-back { background: var(--card-grey); }
  .embossed-art {
    position: absolute;
    right: 0;
    top: 0;
    width: 340px;
    height: 309px;
    background: linear-gradient(120deg, var(--card-grey) 0%, var(--card-grey-light) 55%, var(--card-grey) 100%);
  }
  .brand-mark {
    position: absolute;
    left: 56px;
    top: 170px;
    display: flex;
    align-items: center;
    gap: 10px;
  }
  .brand-mark .dot {
    width: 14px;
    height: 14px;
    background: var(--brand-green);
  }
  .brand-mark .wordmark {
    font-size: 40px;
    font-weight: 700;
    color: var(--brand-green);
    letter-spacing: -0.01em;
  }
</style>
</head>
<body>
<main class="stage">
  <section class="card card-front" aria-label="Business card front">
    <p class="contact-name">NEIL HADLEY<span class="credentials">CA, CPA</span></p>
    <p class="contact-title">Vice President Finance<br>&amp; Chief Financial Officer</p>
    <p class="contact-address">1400, 815 4 Street S.W.<br>Calgary, AB T2P 4K8</p>
    <p class="contact-lines">
      <span class="label">M</span>(403)555-0187<span class="sep">/</span><span class="label">T</span>(587)555-0142<br>
      nhadley@bramwellresources-mail.com
    </p>
    <p class="website">bramwellresources.com</p>
    <p class="name-watermark" aria-hidden="true">Bramwell</p>
  </section>

  <section class="card card-back" aria-label="Business card back">
    <div class="embossed-art" role="img" aria-label="Blind-embossed industrial oil pumpjack illustration"></div>
    <div class="brand-mark">
      <span class="dot"></span>
      <span class="wordmark">Bramwell</span>
    </div>
  </section>
</main>
</body>
</html>
```